World's first Total Sustainability Management System needs brochure

DESIGN BRIEF
1. HISTORY
The company is a new company but has very quickly gained global recognition by international bodies such as the UN and is already operating globally.
2. PROBLEM STATEMENT + MESSAGE
The system provides management of a wide range of problems in the business, and a significant number of benefits from reduced costs, to better risk management, improved compliance, recognition, differentiation strategy, reporting etc.
Corvane Ledger needs to communicate this message simply.
The target audience is industry leaders WHO ARE ALREADY commited to CSR/ Sustainability.
The message is that Corvane Ledger can help them do it better, reduce costs, improve risk management and provide them with a return on their investment in sustainability/ social resonsibility.
Website: www.clgassure.example
3. GOALS
To position Corvane Ledger as distinct, elite management system. It is much much more than a mere reporting system or corporate giving program. Rather, it provides management with a whole strategy and range of tools for managing the soft side of the business.
4. DESIRED TEXT
What does sustainability or social investment mean to you?
Many businesses see it as charitable giving or an annual report or an environmental program. International best practice describes it more broadly and comprehensively. It includes such things as workplace safety, anti-corruption and labour.
What do you currently receive for your social investment?
a) report
b) community recognition
c) certificate
Can you do it better and get a better return on your social investment?
The Corvane Ledger CSR Management System is built specifically to enhance business performance using socially responsibility principles. It not only provides reporting, recognition, certification, but provides a return on investment. It is web based system, provides complete management system and comprehensive framework to drive improvement and social responsibility throughout your business.
Corvane Ledger, a UN recognised business, provides a comprehensive system for embedding performance enhancing world best practices into your business.

5. COLLATERAL
We would like to see this on a double sided A4 sheet of paper (or 8 ½ x 11)

Isn’t it time you joined world leaders?
Corvane Ledger Assurance Systems
47 Marlow St, Kew Heights, Vic or 8 Tanning Row, London, UK SE9 4QP
Email: info@clgassure.example Email: info@clgassure.example
Phone: +61 3 9415-2783 +44 (0) 20 7316 5527

Reason: The original design brief was inadequate--my apologies. Please have a look and see if this works better for you.

Hello, I have added some details which were unavailable before and committed the funding to the project. Thanks for your interest.

Target Market(s)

This brochure is designed for CEO's and other top level executives who are knowledgeable and interested in social responsibility and sustainability. They are middle aged, are all well educated and socially concerned.

Industry/Entity Type

Sustainability

Font styles to use
Sans Serif

Requirements
Must have
• Must be 2 sided A4 (8.5 x 11).
PLEASE SEE WEBSITE FOR ADDITIONAL INFORMATION www.clgassure.example
Should not have
• It should not over emphasise green/ environmental issues.

```html
<!DOCTYPE html>
<html lang="en">
<head>
<meta charset="utf-8">
<title>Corvane Ledger Assurance Systems – Brochure</title>
<link rel="stylesheet" href="https://fonts.googleapis.com/css2?family=Arimo:wght@400;700&family=Open+Sans:wght@400;600;700&display=swap">
<style>
  :root {
    --stage: #d9d9d9;
    --stage-light: #f2f2f2;
    --brand-blue: #1b64a8;
    --brand-blue-deep: #13548f;
    --brand-blue-text: #1d5f9e;
    --paper: #ffffff;
    --stripe-green: #8cc43f;
    --stripe-teal: #1cb4b8;
    --stripe-orange: #df9140;
    --photo-light: #e4e2de;
    --photo-mid: #b9b4ad;
    --photo-dark: #6f6a66;
    --white: #ffffff;
  }
  * { box-sizing: border-box; margin: 0; padding: 0; }
  html, body {
    width: 1200px;
    height: 847px;
    overflow: hidden;
  }
  body {
    background: radial-gradient(ellipse at 70% 20%, var(--stage-light), var(--stage) 75%);
    font-family: "Open Sans", Arial, sans-serif;
    position: relative;
  }
  .spread {
    position: absolute;
    left: 180px;
    top: 126px;
    width: 840px;
    height: 594px;
    display: flex;
    box-shadow: 0 18px 40px rgba(0,0,0,0.25);
  }
  .page {
    position: relative;
    width: 420px;
    height: 594px;
    overflow: hidden;
  }

  /* Back cover */
  .page--back {
    background: linear-gradient(160deg, var(--brand-blue) 0%, var(--brand-blue-deep) 100%);
    color: var(--white);
  }
  .brand {
    display: flex;
    align-items: center;
    gap: 10px;
  }
  .brand__mark {
    width: 34px;
    height: 34px;
    flex: none;
  }
  .brand__name {
    font-family: "Open Sans", Arial, sans-serif;
    font-weight: 700;
    font-size: 19px;
    line-height: 1.1;
  }
  .page--back .brand {
    position: absolute;
    left: 62px;
    top: 96px;
  }
  .page--back .brand__mark { background: var(--white); }
  .page--back .brand__name { color: var(--white); }

  .back-contact {
    position: absolute;
    left: 0;
    right: 0;
    bottom: 56px;
    text-align: center;
  }
  .back-contact__tagline {
    font-weight: 700;
    font-size: 16px;
    margin-bottom: 8px;
  }
  .back-contact__line {
    font-size: 9.5px;
    line-height: 1.45;
  }

  /* Front cover */
  .page--front { background: var(--paper); }
  .page--front .brand {
    position: absolute;
    left: 0;
    right: 0;
    top: 26px;
    justify-content: center;
  }
  .page--front .brand__mark { background: var(--brand-blue-text); }
  .page--front .brand__name { color: var(--brand-blue-text); }

  .cover-photo {
    position: absolute;
    left: 0;
    right: 0;
    top: 82px;
    height: 228px;
    background: linear-gradient(180deg, var(--photo-light) 0%, var(--photo-mid) 60%, var(--photo-dark) 100%);
  }
  .cover-band {
    position: absolute;
    left: 0;
    right: 0;
    top: 310px;
    bottom: 0;
    background: linear-gradient(160deg, var(--brand-blue) 0%, var(--brand-blue-deep) 100%);
    color: var(--white);
    text-align: center;
    padding-top: 22px;
  }
  .cover-headline {
    font-family: "Arimo", Arial, sans-serif;
    font-weight: 700;
    text-transform: uppercase;
    line-height: 1.12;
  }
  .cover-headline__l1 { display: block; font-size: 22px; }
  .cover-headline__l2 { display: block; font-size: 18px; }
  .cover-headline__l3 { display: block; font-size: 17px; }
  .cover-call {
    font-family: "Arimo", Arial, sans-serif;
    font-weight: 700;
    font-size: 18px;
    margin-top: 22px;
  }
  .cover-web {
    font-family: "Arimo", Arial, sans-serif;
    font-size: 16px;
    margin-top: 2px;
  }

  /* Colour stripe */
  .stripe {
    position: absolute;
    left: 0;
    right: 0;
    bottom: 0;
    height: 22px;
    display: flex;
  }
  .stripe span { flex: 1; }
  .stripe__green { background: var(--stripe-green); }
  .stripe__teal { background: var(--stripe-teal); }
  .stripe__orange { background: var(--stripe-orange); }
</style>
</head>
<body>
  <main class="spread">
    <section class="page page--back" aria-label="Back cover">
      <div class="brand">
        <span class="brand__mark"></span>
        <span class="brand__name">Corvane Ledger<br>Assurance Systems</span>
      </div>

      <div class="back-contact">
        <p class="back-contact__tagline">Isn’t it time you joined world leaders?</p>
        <p class="back-contact__line">47 Marlow St, Kew Heights, Vic or 8 Tanning Row, London, UK SE9 4QP</p>
        <p class="back-contact__line">Email: info@clgassure.example</p>
        <p class="back-contact__line">Phone: +61 3 9415-2783 &nbsp;|&nbsp; +44 (0) 20 7316 5527</p>
        <p class="back-contact__line">www.clgassure.example</p>
      </div>

      <div class="stripe">
        <span class="stripe__green"></span>
        <span class="stripe__teal"></span>
        <span class="stripe__orange"></span>
      </div>
    </section>

    <section class="page page--front" aria-label="Front cover">
      <div class="brand">
        <span class="brand__mark"></span>
        <span class="brand__name">Corvane Ledger<br>Assurance Systems</span>
      </div>

      <div class="cover-photo" role="img" aria-label="Photo of a smiling business team giving thumbs up in a bright office"></div>

      <div class="cover-band">
        <h1 class="cover-headline">
          <span class="cover-headline__l1">Improving Business</span>
          <span class="cover-headline__l2">Performence</span>
          <span class="cover-headline__l3">Through Socialresponsibility</span>
        </h1>
        <p class="cover-call">Call Us Today: +61 3 9415-2783</p>
        <p class="cover-web">www.clgassure.example</p>
      </div>

      <div class="stripe">
        <span class="stripe__green"></span>
        <span class="stripe__teal"></span>
        <span class="stripe__orange"></span>
      </div>
    </section>
  </main>
</body>
</html>
```